Design a Tallow Loom Museum + exhibition design**

I'm creating an Online Museum of Tallow Loom which will tell the story of hemp from ancient times to now and the future
cover the medical, industrial and nutritional uses and development of hemp
the people behind it, researchers, politicians, farmers and influencerts

the museum will have a number of "wings" , each holds an exhibition around a differnet theme, for example:

Hemp in the Age of Empires: 18th and 19th Century Collections
Hemp - The History of Healing
Domestication and Early Use: Ancient Collection
From Cotton Gin to Plastics and Prohibition: Hemp's Decline

these are just a few sample ideas for exhibitions

I'm looking for an overall design for the museum home page and exhibition page which will make people curious and want to spend time,learning and browsing

Think mobile -first :)

You are requested to design

1. Home page
2. Exhibition page

Target Market(s)

Hemp aficionados, curious fans

Logo Text

The Tallow Loom Museum

Coding

Coded - Design and coding required

Number of Pages Required

3 page

Font styles to use
Sans Serif
Decorative

Requirements
Must have
• a homepage design which prompts visitors to immediately start watching an exhibition

visitors need to understand that this is a museum , so that they dont think it's a business, a service provider or anything like that

needs to have the usual links to T&C, privacy, about us

needs to have a link to "Leave by the curio stall"

must have a visual WOW effect
Nice to have
• animations, sounds etc
Should not have
• forms like contact us etc - not relevant

```html
<!DOCTYPE html>
<html lang="en">
<head>
<meta charset="utf-8">
<title>LOOMHALL — The Tallow Loom Museum</title>
<link rel="stylesheet" href="https://fonts.googleapis.com/css2?family=Bebas+Neue&family=Barlow:wght@400;500&family=Roboto:wght@400&display=swap">
<style>
:root{
  --green:#1a7f1c;
  --ink:#2b2b2b;
  --text:#444;
  --white:#fff;
  --black:#0d0d0d;
  --rule:#222;
}
*{box-sizing:border-box;margin:0;padding:0}
html,body{width:1200px;height:3426px;overflow:hidden}
body{font-family:"Barlow",Arial,sans-serif;color:var(--text);background:var(--white);position:relative}
.display{font-family:"Bebas Neue",Impact,sans-serif;font-weight:400;letter-spacing:.5px}
section,header{position:relative;width:1200px}

.topbar{height:57px;background:var(--green);color:var(--white);display:flex;align-items:center;justify-content:center;font-size:24px}

.site-header{height:123px;display:flex;align-items:center;justify-content:space-between;padding:0 111px}
.brand{font-size:62px;color:var(--ink);line-height:1;padding-top:6px}
.main-nav{display:flex;gap:43px}
.main-nav a{font-size:17px;color:var(--ink);text-decoration:none}
.main-nav a.active{color:var(--green)}

.hero{height:695px;background:radial-gradient(ellipse at 75% 30%,#2f5a31 0%,#183019 35%,#0c120c 70%,#070907 100%);text-align:center;color:var(--white)}
.hero-title{position:absolute;left:0;right:0;top:240px;font-size:106px;line-height:1}
.hero-sub{position:absolute;left:0;right:0;top:348px;font-size:60px;line-height:1;color:var(--green)}
.play{position:absolute;left:552px;top:419px}

.history{height:537px}
.section-title{font-size:42px;color:var(--ink);line-height:1}
.section-title em{font-style:normal;color:var(--green)}
.short-rule{width:40px;height:2px;background:var(--rule)}
.history .section-title{position:absolute;left:111px;top:95px}
.history .short-rule{position:absolute;left:111px;top:149px}
.history .copy{position:absolute;left:111px;top:175px;width:463px;font-size:14px;line-height:26px;text-align:justify}
.history .copy p+p{margin-top:32px}
.leaf{position:absolute;left:625px;top:98px;width:448px;height:388px;background:radial-gradient(ellipse at 50% 50%,#3e7a36 0%,#5b9a4c 35%,#fff 70%)}

.collection{height:624px;background:linear-gradient(135deg,#1f8a20,#16761a 60%,#1b801d);text-align:center}
.collection .section-title{color:var(--white);position:absolute;left:0;right:0;top:62px;font-size:46px}
.collection .short-rule{background:var(--white);position:absolute;left:580px;top:121px}
.cards{position:absolute;left:111px;top:162px;display:flex;gap:24px}
.card{width:311px;height:388px;background:var(--white);padding:10px}
.card-photo{height:206px}
.card-title{font-size:23px;color:var(--ink);margin-top:26px}
.card-text{font-family:"Roboto",Arial,sans-serif;font-size:13.5px;line-height:26px;padding:8px 10px 0}

.decline{height:665px}
.decline-photo{position:absolute;left:125px;top:84px;width:501px;height:413px;background:linear-gradient(180deg,#cfe2f3 0%,#e9eef0 35%,#8aa93a 55%,#5d7d1f 80%,#3f5c15 100%)}
.decline-card{position:absolute;left:543px;top:197px;width:534px;height:396px;background:var(--white);box-shadow:0 0 6px rgba(0,0,0,.12);padding:38px 35px 0 40px}
.decline-card .short-rule{margin:12px 0 0}
.decline-card .copy{font-family:"Roboto",Arial,sans-serif;font-size:13.5px;line-height:26px;margin-top:18px;text-align:justify}
.btn-solid{display:inline-block;margin-top:26px;width:152px;height:50px;line-height:52px;text-align:center;background:var(--green);color:var(--white);font-size:22px;text-decoration:none}

.cta{height:412px;background:linear-gradient(100deg,#141a14 0%,#1d2c1d 40%,#2d4a2c 70%,#172217 100%);color:var(--white)}
.cta-lines{position:absolute;left:111px;top:130px;font-size:36px;line-height:50px}
.btn-outline{position:absolute;left:111px;top:243px;width:153px;height:49px;border:2px solid var(--white);color:var(--white);text-decoration:none;text-align:center;line-height:48px;font-size:24px}

.site-footer{height:313px;background:var(--black);color:var(--white);text-align:center;position:relative}
.footer-brand{position:absolute;left:0;right:0;top:58px;font-size:60px;line-height:1}
.footer-nav{position:absolute;left:0;right:0;top:146px;display:flex;justify-content:center;gap:43px}
.footer-nav a{color:var(--white);text-decoration:none;font-size:17px}
.share-links{position:absolute;left:0;right:0;top:200px;display:flex;justify-content:center;gap:6px}
.share-links a{width:37px;height:37px;border:2px solid var(--white);border-radius:50%;display:flex;align-items:center;justify-content:center}
.share-links svg{width:17px;height:17px;fill:none;stroke:var(--white);stroke-width:2;stroke-linecap:round;stroke-linejoin:round}
.legal{position:absolute;left:0;right:0;top:256px;font-size:17px}
</style>
</head>
<body>

<div class="topbar display">"Leave by the curio stall"</div>

<header class="site-header">
  <div class="brand display">LOOMHALL</div>
  <nav class="main-nav display">
    <a href="#" class="active">Home</a><a href="#">About us</a><a href="#">Exhibitions</a><a href="#">Collection</a><a href="#">Gallery</a><a href="#">Curio Stall</a>
  </nav>
</header>

<section class="hero" role="img" aria-label="Dark close-up photograph of green plant leaves">
  <h1 class="hero-title display">LOOMHALL</h1>
  <p class="hero-sub display">18th &amp; 19th Century Collections</p>
  <svg class="play" width="96" height="96" viewBox="0 0 96 96" aria-label="Play exhibition video">
    <circle cx="48" cy="48" r="46" fill="none" stroke="#fff" stroke-width="3"/>
    <path d="M38 32 L66 48 L38 64 Z" fill="#fff"/>
  </svg>
</section>

<section class="history">
  <h2 class="section-title display">The History <em>of Healing</em></h2>
  <div class="short-rule"></div>
  <div class="copy">
    <p>The French Resistance: still growing during prohibition despite UN pressure As a food In 2000, highly controlled hemp returned to US stores as a legal food good As a textile China's Great Leap Forward to dominate textile production including (banned elsewhere) hemp</p>
    <p>Sed ut perspiciatis unde omnis iste natus error sit voluptatem accusantium doloremque laudantium, totam rem aperiam, eaque ipsa quae ab illo inventore veritatis et quasi architecto beatae vitae dicta sunt explicabo. Nemo enim ipsam voluptatem quia voluptas sit aspernatur aut odit aut fugit, sed quia consequuntur magni dolores eos qui ratione voluptatem sequi nesciunt.</p>
  </div>
  <div class="leaf" role="img" aria-label="Illustration of a single green plant leaf"></div>
</section>

<section class="collection">
  <h2 class="section-title display">Ancient Collection</h2>
  <div class="short-rule"></div>
  <div class="cards">
    <article class="card">
      <div class="card-photo" role="img" aria-label="Photograph of a gloved hand holding a plant bud" style="background:linear-gradient(135deg,#5f8fc4,#3e6fa8 45%,#6d8a4a 70%,#c7d3de)"></div>
      <h3 class="card-title display">Sed ut perspiciatis unde</h3>
      <p class="card-text">Nemo enim ipsam voluptatem quia voluptas sit aspernatur aut odit aut fugit, sed quia co voluptatem sequi nesciunt.</p>
    </article>
    <article class="card">
      <div class="card-photo" role="img" aria-label="Photograph of gloved hands among green leaves" style="background:linear-gradient(135deg,#1d4a1f,#2f7a2a 50%,#1a3d1a)"></div>
      <h3 class="card-title display">Sed ut perspiciatis unde</h3>
      <p class="card-text">Nemo enim ipsam voluptatem quia voluptas sit aspernatur aut odit aut fugit, sed quia co voluptatem sequi nesciunt.</p>
    </article>
    <article class="card">
      <div class="card-photo" role="img" aria-label="Photograph of a hand raising a leaf against a sunny field" style="background:linear-gradient(180deg,#9fb7cf,#e3ecef 45%,#9aa257 78%,#6b6f2c)"></div>
      <h3 class="card-title display">Sed ut perspiciatis unde</h3>
      <p class="card-text">Nemo enim ipsam voluptatem quia voluptas sit aspernatur aut odit aut fugit, sed quia co voluptatem sequi nesciunt.</p>
    </article>
  </div>
</section>

<section class="decline">
  <div class="decline-photo" role="img" aria-label="Photograph of a plant field under a blue sky"></div>
  <div class="decline-card">
    <h2 class="section-title display">Hemp's <em>Decline</em></h2>
    <div class="short-rule"></div>
    <p class="copy">Sed ut perspiciatis unde omnis iste natus error sit voluptatem accusantium doloremque laudantium, totam rem aperiam, eaque ipsa quae ab illo inventore veritatis et quasi architecto beatae vitae dicta sunt explicabo. Nemo enim ipsam voluptatem quia voluptas sit aspernatur aut odit aut fugit, sed quia consequuntur magni dolores eos qui ratione voluptatem sequi nesciunt. Neque porro quisquam est, qui dolorem ipsum quia dolor sit amet, consectetur labore et dolore magnam aliquam quaerat voluptatem.</p>
    <a href="#" class="btn-solid display">Read more</a>
  </div>
</section>

<section class="cta" role="img" aria-label="Dark blurred photograph of plant leaves">
  <div class="cta-lines display">Sed ut perspiciatis unde<br>Omnis iste natus error sit voluptatem</div>
  <a href="#" class="btn-outline display">Learn more</a>
</section>

<footer class="site-footer">
  <div class="footer-brand display">LOOMHALL</div>
  <nav class="footer-nav display">
    <a href="#">Home</a><a href="#">About us</a><a href="#">Exhibitions</a><a href="#">Collection</a><a href="#">Gallery</a><a href="#">Curio Stall</a>
  </nav>
  <div class="share-links">
    <a href="#" aria-label="Email"><svg viewBox="0 0 24 24"><rect x="3" y="5" width="18" height="14" rx="1"/><path d="M3 6l9 7 9-7"/></svg></a>
    <a href="#" aria-label="Share"><svg viewBox="0 0 24 24"><circle cx="6" cy="12" r="2.5"/><circle cx="18" cy="6" r="2.5"/><circle cx="18" cy="18" r="2.5"/><path d="M8.2 10.8l7.6-3.6M8.2 13.2l7.6 3.6"/></svg></a>
    <a href="#" aria-label="Guestbook"><svg viewBox="0 0 24 24"><path d="M4 5h16v11H9l-5 4z"/></svg></a>
    <a href="#" aria-label="Location"><svg viewBox="0 0 24 24"><path d="M12 21s-6-6.5-6-11a6 6 0 0112 0c0 4.5-6 11-6 11z"/><circle cx="12" cy="10" r="2"/></svg></a>
    <a href="#" aria-label="Watch"><svg viewBox="0 0 24 24"><path d="M8 5l11 7-11 7z"/></svg></a>
  </div>
  <p class="legal display">© Copyrights 2021 LOOMHALL. All rights reserved.Privacy Policy Terms and Conditions</p>
</footer>

</body>
</html>
```